Alcohol free flavoured Malt Drink Label design

we are beverage company producer our main brand is Brightwave, we are willing to produce Alcohol free flavoured Malt Drink, this product target new generation should be fresh colourful and modern, the name of the Malt drink is Zeal. so main brand is Brightwave and product name is ZEAL. the label size: 198mm X 66mm

Dear All
i changed the product name to NUR (means Crown ) this will add more ideas in the design . Thanks

```html
<!DOCTYPE html>
<html lang="en">
<head>
<meta charset="utf-8">
<title>Brightwave Zeal – Alcohol Free Flavoured Malt</title>
<link rel="stylesheet" href="https://fonts.googleapis.com/css2?family=Montserrat:wght@500;800&family=Titan+One&display=swap">
<style>
  :root {
    --forest: #2d6e50;
    --green: #00944a;
    --lime: #96c83e;
    --lime-soft: #b5dc6a;
    --cream: #faf5e6;
    --white: #ffffff;
    --label-white: #f2f2f0;
    --text-green: #2fa866;
    --hop-tone: #1f8a4f;
  }
  * { margin: 0; padding: 0; box-sizing: border-box; }
  html, body {
    width: 1200px;
    height: 400px;
    overflow: hidden;
    background: var(--cream);
  }
  .banner {
    position: relative;
    width: 1200px;
    height: 400px;
    overflow: hidden;
  }
  .banner-waves { position: absolute; inset: 0; }
  .wave-forest { fill: var(--forest); }
  .wave-green { fill: var(--green); }
  .wave-lime { fill: var(--lime); }
  .wave-cream { fill: var(--cream); }
  .bubble { fill: none; stroke: var(--white); stroke-width: 1.2; }
  .hop-placeholder { fill: var(--hop-tone); opacity: 0.55; }

  .label {
    position: absolute;
    left: 330px;
    top: 60px;
    width: 540px;
    height: 180px;
    overflow: hidden;
    box-shadow: 0 8px 24px rgba(0, 0, 0, 0.18);
  }
  .label-art { position: absolute; inset: 0; }
  .label-green { fill: var(--green); }
  .label-lime { fill: var(--lime); }
  .label-white { fill: var(--label-white); }
  .label-bubble { fill: none; stroke: var(--white); stroke-width: 1; opacity: 0.8; }

  .brand-name {
    position: absolute;
    top: 16px;
    left: 0;
    width: 100%;
    text-align: center;
    font-family: "Montserrat", sans-serif;
    font-weight: 800;
    font-size: 26px;
    color: var(--white);
    letter-spacing: 0.5px;
  }
  .product-name {
    position: absolute;
    top: 58px;
    left: 0;
    width: 100%;
    text-align: center;
    font-family: "Titan One", sans-serif;
    font-size: 64px;
    line-height: 1;
    color: var(--lime-soft);
    letter-spacing: 4px;
  }
  .product-type {
    position: absolute;
    bottom: 14px;
    left: 0;
    width: 100%;
    text-align: center;
    font-family: "Montserrat", sans-serif;
    font-weight: 500;
    font-size: 12px;
    line-height: 1.3;
    letter-spacing: 1.5px;
    color: var(--text-green);
    text-transform: uppercase;
  }
</style>
</head>
<body>
<main class="banner">
  <svg class="banner-waves" width="1200" height="400" viewBox="0 0 1200 400" aria-hidden="true">
    <rect class="wave-forest" x="0" y="0" width="1200" height="400"/>
    <path class="wave-green" d="M0 95 C90 90 150 50 240 55 C330 60 380 110 470 90 C560 70 640 40 760 50 C880 60 920 75 1010 65 C1090 55 1150 20 1200 0 L1200 400 L0 400 Z"/>
    <path class="wave-lime" d="M0 170 C60 155 110 160 150 200 C190 240 230 270 300 230 C360 195 400 150 470 160 C540 170 600 180 640 200 L1200 200 L1200 400 L0 400 Z"/>
    <path class="wave-cream" d="M0 175 C50 170 90 180 120 220 C150 260 180 290 250 250 C320 210 380 210 440 220 C520 232 600 240 680 250 L880 255 C940 255 980 200 1020 165 C1060 135 1110 150 1150 140 C1175 135 1190 130 1200 128 L1200 400 L0 400 Z"/>
    <g class="bubbles">
      <circle class="bubble" cx="118" cy="165" r="4"/>
      <circle class="bubble" cx="182" cy="165" r="7"/>
      <circle class="bubble" cx="140" cy="212" r="22"/>
      <circle class="bubble" cx="240" cy="240" r="40"/>
      <circle class="bubble" cx="272" cy="190" r="5"/>
      <circle class="bubble" cx="78" cy="180" r="3"/>
      <circle class="bubble" cx="880" cy="225" r="30"/>
      <circle class="bubble" cx="963" cy="133" r="19"/>
      <circle class="bubble" cx="926" cy="165" r="4"/>
      <circle class="bubble" cx="966" cy="176" r="4"/>
      <circle class="bubble" cx="1038" cy="160" r="12"/>
      <circle class="bubble" cx="1045" cy="117" r="4"/>
      <circle class="bubble" cx="1154" cy="81" r="7"/>
      <circle class="bubble" cx="1180" cy="81" r="3"/>
      <circle class="bubble" cx="1177" cy="109" r="5"/>
      <circle class="bubble" cx="1200" cy="165" r="40"/>
    </g>
    <g class="hops">
      <rect class="hop-placeholder" x="28" y="55" width="50" height="95" rx="25" role="img" aria-label="Line drawing of a malt hop cone"/>
      <rect class="hop-placeholder" x="322" y="120" width="50" height="95" rx="25" role="img" aria-label="Line drawing of a malt hop cone"/>
      <rect class="hop-placeholder" x="844" y="30" width="48" height="95" rx="24" role="img" aria-label="Line drawing of a malt hop cone"/>
      <rect class="hop-placeholder" x="1075" y="70" width="50" height="95" rx="25" role="img" aria-label="Line drawing of a malt hop cone"/>
    </g>
  </svg>

  <section class="label" aria-label="Zeal can label">
    <svg class="label-art" width="540" height="180" viewBox="0 0 540 180" aria-hidden="true">
      <rect class="label-green" x="0" y="0" width="540" height="180"/>
      <path class="label-lime" d="M0 95 C120 55 300 45 540 70 L540 180 L0 180 Z"/>
      <path class="label-white" d="M0 135 C120 100 330 95 540 115 L540 180 L0 180 Z"/>
      <circle class="label-bubble" cx="120" cy="70" r="7"/>
      <circle class="label-bubble" cx="200" cy="60" r="3"/>
      <circle class="label-bubble" cx="420" cy="55" r="5"/>
      <circle class="label-bubble" cx="470" cy="72" r="3"/>
      <circle class="label-bubble" cx="60" cy="88" r="4"/>
    </svg>
    <p class="brand-name">Brightwave</p>
    <h1 class="product-name">ZEAL</h1>
    <p class="product-type">Alcohol Free<br>Flavoured Malt</p>
  </section>
</main>
</body>
</html>
```